Business Card Design

Hottest Internet Based Blues Radio Station in Southwest Florida All Blues 24/7 Real Authentic Blues Classic and Modern

Industry/Entity Type

Business

Contact Information for Business Card

Marco "Tall Ned" Okafor
The Harbor Wave Media, Inc.
512 Willow Crest Lane
Port Alder, FL 34012

```html
<!DOCTYPE html>
<html lang="en">
<head>
<meta charset="utf-8">
<title>The Harbor Wave Media, Inc. — Business Card</title>
<link rel="stylesheet" href="https://fonts.googleapis.com/css2?family=Cinzel:wght@400;600&display=swap">
<style>
  :root {
    --stage: #3a3a3a;
    --card: #060606;
    --ink: #f4f1ea;
    --amber: #eea032;
    --rule: #ffffff;
  }
  * { margin: 0; padding: 0; box-sizing: border-box; }
  html, body {
    width: 1200px; height: 900px; overflow: hidden;
    background: var(--stage);
    font-family: "Cinzel", Georgia, serif;
  }
  .stage {
    width: 1200px; height: 900px;
    display: flex; flex-direction: column; align-items: center; justify-content: center;
    gap: 32px;
  }
  .card {
    position: relative;
    width: 720px; height: 412px;
    background: var(--card);
    border-radius: 22px;
    overflow: hidden;
    box-shadow: 0 10px 28px rgba(0,0,0,.45);
  }

  .brand-mark {
    position: absolute;
    display: flex; align-items: center; gap: 14px;
  }
  .brand-mark .ring {
    width: 74px; height: 74px; border-radius: 50%;
    border: 2px solid var(--ink);
    flex: none;
  }
  .brand-name {
    color: var(--ink);
    font-weight: 600;
    letter-spacing: .04em;
    line-height: 1.05;
    text-transform: uppercase;
    white-space: nowrap;
  }

  /* front */
  .front .brand-mark { left: 110px; top: 120px; }
  .front .brand-name { font-size: 26px; }
  .front .tagline {
    position: absolute; left: 110px; top: 250px;
    color: var(--ink); font-size: 19px; letter-spacing: .05em;
    text-transform: uppercase; white-space: nowrap;
  }

  /* back */
  .back .brand-mark { left: 70px; top: 250px; }
  .back .brand-name { font-size: 24px; }
  .holder {
    position: absolute; right: 64px; top: 70px;
    color: var(--ink); font-size: 27px; font-weight: 400; letter-spacing: .05em;
    text-transform: uppercase; text-align: right; white-space: nowrap;
  }
  .contact {
    position: absolute; right: 40px; top: 128px;
    list-style: none;
    color: var(--amber);
    font-size: 15px; letter-spacing: .04em;
    font-variant: small-caps;
    text-align: right;
  }
  .contact li { display: flex; justify-content: flex-end; align-items: center; gap: 10px; height: 24px; white-space: nowrap; }
  .contact li .icon { width: 14px; height: 14px; flex: none; }
  .contact li .spacer { width: 14px; flex: none; }
  .contact .gap { margin-top: 12px; }
  .contact .email { text-transform: uppercase; font-size: 13px; }
  .base-rule {
    position: absolute; left: 0; right: 0; bottom: 32px;
    height: 3px; background: var(--rule);
  }
  .base-band {
    position: absolute; left: 0; right: 0; bottom: 0;
    height: 26px; background: var(--amber);
  }
</style>
</head>
<body>
<main class="stage">

  <section class="card front" aria-label="Card front">
    <div class="brand-mark">
      <span class="ring"></span>
      <span class="brand-name">The Harbor Wave<br>Media, Inc.</span>
    </div>
    <p class="tagline">All Blues, All Night, All Soul</p>
  </section>

  <section class="card back" aria-label="Card back">
    <div class="brand-mark">
      <span class="ring"></span>
      <span class="brand-name">The Harbor Wave<br>Media, Inc.</span>
    </div>

    <h1 class="holder">Marco "Tall Ned" Okafor</h1>

    <ul class="contact">
      <li><span>512 Willow Crest Lane</span><span class="spacer"></span></li>
      <li><span>Port Alder, FL 34012</span><span class="spacer"></span></li>
      <li class="gap">
        <span>+1 555 014-2290</span>
        <svg class="icon" viewBox="0 0 16 16" aria-hidden="true"><path d="M4 1.5l2.2 3-1.4 1.6c.8 1.8 2.3 3.3 4.1 4.1l1.6-1.4 3 2.2-1.2 2.4C6.8 13.2 2.8 9.2 1.6 2.7z" fill="none" stroke="#f4f1ea" stroke-width="1.3" stroke-linejoin="round"/></svg>
      </li>
      <li>
        <span class="email">info@harborwavemedia.com</span>
        <svg class="icon" viewBox="0 0 16 16" aria-hidden="true"><rect x="1.5" y="3.5" width="13" height="9" fill="none" stroke="#f4f1ea" stroke-width="1.3"/><path d="M1.5 3.5L8 9l6.5-5.5" fill="none" stroke="#f4f1ea" stroke-width="1.3"/></svg>
      </li>
    </ul>

    <div class="base-rule"></div>
    <div class="base-band"></div>
  </section>

</main>
</body>
</html>
```